My dad's 70th birthday party invite - Greek theme!

My dad isn't actually Greek, but his party will be at a Greek restaurant, so we thought it'd be a fun to have a Greek theme for the invitation to his 70th birthday party.

The invite will be sent out by email, so it needs to look good on screen, AND when it's printed out by the recipients, likely onto A4 paper and put up on a noticeboard/stuck to the fridge as a reminder etc.
Updates

Reason: A designer has asked us to extend the deadline and as we're not in a rush to complete this particular project, we've done so. Thanks everyone for their designs to date.

Target Market(s)

my dad's friends and family - average 50-70years old

Industry/Entity Type

Restaurant

Requirements
Must have
• For: Brannick's 70th birthday
Date: 30 Nov 2013
Time: 7.30pm
Place: Lymora Taverna, 47 Tressendale Road, Mulvaney Park

RSVP by: Friday 1 November
to: kat@pqx-example.com.au
(Please also let us know of any specific dietary requirements eg vegetarian, seafood allergy etc. Thanks. And please, no presents - just really hoping you can join us on the night!)
Nice to have
• Some ideas for you:
- he loves the blue & white of Greece eg white buildings against blue ocean, Greek flag etc
- and red geraniums/pink bouganvillea - quintessential (yet stylish!) Greece
- also, maybe you could use the names of the dishes we'll be having for dinner somehow? ie:
MEZES
Taramosalata
Tzatziki
Skordalia
Hommus
Haloumi
Psití Melitzána
Pita
Eliés
Dolmathes
THALASINA
Chtapódi Psitó
KalamáriaTiganitá
KREATA
Souvlaki
Arní
Lachaniká se Sáltsa - Verrosti
SALATA
Baklava
Paximádi Rolá
Kataifi
Kourabiethes
Greek Coffee

Hope that helps!
Should not have
• We'd prefer a simple colour scheme, ie not too many different colours.

```html
<!DOCTYPE html>
<html lang="en">
<head>
<meta charset="utf-8">
<title>Brannick's 70th Birthday Invitation</title>
<link rel="stylesheet" href="https://fonts.googleapis.com/css2?family=Cinzel:wght@400;700&family=EB+Garamond:ital,wght@0,400;0,600;1,600&display=swap">
<style>
  :root {
    --sky-top: #6cc3ef;
    --sky-mid: #def3fb;
    --sea: #29c4d6;
    --sea-deep: #12b6cc;
    --key-teal: #1fa9b0;
    --ink-navy: #1c3c8c;
    --ink-dark: #2b2b3a;
    --ink-grey: #3c3c46;
    --white: #ffffff;
    --geranium-red: #d9322b;
    --leaf-green: #4f8a3a;
    --town-white: #e9ecef;
    --town-shade: #c9d1d8;
  }
  * { margin: 0; padding: 0; box-sizing: border-box; }
  html, body { width: 837px; height: 1200px; overflow: hidden; background: var(--white); }
  .invitation {
    position: relative;
    width: 837px;
    height: 1200px;
    overflow: hidden;
    background:
      linear-gradient(180deg, rgba(255,255,255,0) 78%, var(--sea) 84%, var(--sea-deep) 100%),
      radial-gradient(ellipse at 35% 30%, var(--white) 0%, var(--sky-mid) 40%, var(--sky-top) 100%);
    font-family: "EB Garamond", Georgia, serif;
  }
  .key-frame { position: absolute; left: 32px; top: 40px; width: 776px; height: 1125px; }
  .geraniums {
    position: absolute; left: 482px; top: 115px; width: 298px; height: 505px;
    background: linear-gradient(180deg, var(--geranium-red) 0%, var(--leaf-green) 55%, var(--geranium-red) 100%);
  }
  .harbour-town {
    position: absolute; left: 62px; top: 760px; width: 718px; height: 220px;
    background: linear-gradient(180deg, var(--town-white) 0%, var(--town-shade) 100%);
  }
  .headline {
    position: absolute; left: 130px; top: 117px; width: 270px;
    text-align: center; font-family: "Cinzel", "Times New Roman", serif;
    font-size: 24px; line-height: 30px; font-weight: 400;
    color: var(--ink-dark); letter-spacing: 1px;
  }
  .key-wreath { position: absolute; left: 128px; top: 192px; width: 304px; height: 250px; }
  .honoree {
    position: absolute; left: 170px; top: 212px; width: 220px; text-align: center;
    font-family: "Cinzel", "Times New Roman", serif; font-weight: 700; color: var(--ink-navy);
  }
  .honoree-name { font-size: 30px; line-height: 38px; }
  .honoree-age { font-size: 62px; line-height: 72px; }
  .honoree-age sup {
    font-family: "EB Garamond", Georgia, serif; font-style: italic; font-weight: 600;
    font-size: 38px; vertical-align: 22px; margin-left: 2px;
  }
  .honoree-occasion { font-size: 28px; line-height: 34px; }
  .event-details { position: absolute; left: 90px; top: 470px; width: 390px; text-align: center; color: var(--ink-navy); }
  .event-date { font-size: 17px; line-height: 34px; font-weight: 600; }
  .event-date strong { font-size: 22px; font-weight: 600; }
  .event-time { font-size: 22px; line-height: 30px; font-weight: 600; }
  .event-time small { font-size: 15px; }
  .event-venue { font-size: 16px; line-height: 30px; font-weight: 600; }
  .rsvp-notes {
    position: absolute; left: 105px; top: 607px; width: 340px;
    text-align: center; font-size: 15px; line-height: 20px; color: var(--ink-grey);
  }
  .rsvp-notes p + p { margin-top: 18px; }
  .closing-note {
    position: absolute; left: 62px; top: 1056px; width: 718px; text-align: center;
    font-style: italic; font-weight: 600; font-size: 18px; color: var(--white);
  }
</style>
</head>
<body>
<main class="invitation">
  <svg class="key-frame" viewBox="0 0 776 1125" role="img" aria-label="Greek key border framing the invitation">
    <path fill="var(--key-teal)" fill-rule="evenodd" opacity="0.8"
      d="M0 0H776V1125H0Z M28 28V1097H748V28Z"/>
  </svg>

  <div class="geraniums" role="img" aria-label="Illustration of red geraniums with green leaves"></div>
  <div class="harbour-town" role="img" aria-label="Illustration of a whitewashed Greek harbour town on a hillside above the sea"></div>

  <h1 class="headline">You are invited<br>to celebrate</h1>

  <svg class="key-wreath" viewBox="0 0 304 250" role="img" aria-label="Circular Greek key wreath">
    <path d="M58 12 A140 130 0 1 0 246 12" fill="none" stroke="var(--key-teal)" stroke-width="12" opacity="0.85"/>
  </svg>

  <div class="honoree">
    <div class="honoree-name">Brannick's</div>
    <div class="honoree-age">70<sup>th</sup></div>
    <div class="honoree-occasion">Birthday</div>
  </div>

  <section class="event-details">
    <p class="event-date">Saturday <strong>November 30,</strong> 2013</p>
    <p class="event-time">7.30 <small>PM</small></p>
    <p class="event-venue">Lymora Taverna, 47 Tressendale Road, Mulvaney Park</p>
  </section>

  <section class="rsvp-notes">
    <p>Plese RSVP by Friday 1 November<br>to: kat@pqx-example.com.au</p>
    <p>Please also let us know of any specific<br>dietary requirements<br>eg vegetarian, seafood allergy etc.</p>
  </section>

  <p class="closing-note">And please, no presents - just really hoping you can join us on the night!</p>
</main>
</body>
</html>
```